I want a minimal signage design for my pool service company.

Design a premium modern lower-door decal/wrap for a graphite Marrick Dunefield dual cab ute.
The design should look tough, clean and high-end. Think factory/OEM style graphics rather than a typical tradie signwriting setup.
Style:
* Modern and aggressive
* Minimal but eye-catching
* Fluro/electric blue accents
* Suit graphite grey paint
* Motorsport / Velden Kestrel inspired
* Premium marine/pool industry feel
Placement:
* Runs across the lower section of both doors
* Can slightly extend toward rear tray/front guard
* Must flow nicely with the shape of the ute
Include:
* Lakeshore Tide Care logo
* 0491 358 217
Avoid:
* Big rectangular blocks
* Cheap-looking wrap styles
* Too much text
* Overly busy graphics
The design should look professional enough that it could suit a high-end branded company vehicle while still standing out on the road.
Needs to be a ai/pdf/svg file and dimensions will be about 1600mm x 200mm
Pool service

```html
<!DOCTYPE html>
<html lang="en">
<head>
<meta charset="utf-8">
<title>Lakeshore Tide Care – Lower Door Decal Options</title>
<link rel="stylesheet" href="https://fonts.googleapis.com/css2?family=Roboto+Condensed:wght@700&display=swap">
<style>
  :root {
    --canvas: #ffffff;
    --navy: #0c1457;
    --pool-light: #4fd3ee;
    --pool-mid: #1aa8d6;
    --pool-deep: #0a78b8;
    --trim: #ffffff;
  }
  html, body {
    margin: 0;
    padding: 0;
    width: 1200px;
    height: 1200px;
    overflow: hidden;
    background: var(--canvas);
  }
  .sheet {
    position: relative;
    width: 1200px;
    height: 1200px;
  }
  .decal {
    position: absolute;
    left: 50px;
    width: 1100px;
    font-family: "Roboto Condensed", "Arial Narrow", sans-serif;
    font-weight: 700;
  }
  .decal svg {
    position: absolute;
    inset: 0;
    width: 100%;
    height: 100%;
    display: block;
  }
  .decal-swoosh { top: 300px; height: 200px; }
  .decal-band   { top: 720px; height: 124px; }

  .phone, .brand-name {
    position: absolute;
    margin: 0;
    white-space: nowrap;
    line-height: 1;
  }
  .decal-swoosh .phone {
    left: 36px;
    top: 78px;
    font-size: 50px;
    letter-spacing: 3px;
    color: var(--trim);
  }
  .decal-swoosh .brand-name {
    left: 640px;
    top: 128px;
    font-size: 40px;
    color: var(--navy);
  }
  .decal-band .phone {
    left: 44px;
    top: 40px;
    font-size: 44px;
    letter-spacing: 3px;
    color: var(--navy);
  }
  .decal-band .brand-name {
    left: 560px;
    top: 44px;
    font-size: 44px;
    color: var(--navy);
  }
</style>
</head>
<body>
<main class="sheet">

  <section class="decal decal-swoosh">
    <svg viewBox="0 0 1100 200" preserveAspectRatio="none" aria-hidden="true">
      <defs>
        <linearGradient id="pool-water-a" x1="0" y1="0" x2="1" y2="1">
          <stop offset="0" stop-color="var(--pool-light)"/>
          <stop offset="0.55" stop-color="var(--pool-mid)"/>
          <stop offset="1" stop-color="var(--pool-deep)"/>
        </linearGradient>
      </defs>
      <path class="water-panel" role="img" aria-label="Pool water texture with beach umbrella accents"
            d="M300,200 C520,150 760,110 1100,80 L1100,200 Z"
            fill="url(#pool-water-a)"/>
      <path class="swoosh-navy"
            d="M0,24 C230,14 460,52 690,112 C480,150 220,190 0,200 Z"
            fill="var(--navy)"/>
      <path class="swoosh-trim"
            d="M0,24 C230,14 460,52 690,112 C830,92 960,84 1100,80"
            fill="none" stroke="var(--trim)" stroke-width="5"/>
    </svg>
    <p class="phone">0491 358 217</p>
    <p class="brand-name">lakeshore tide care</p>
  </section>

  <section class="decal decal-band">
    <svg viewBox="0 0 1100 124" preserveAspectRatio="none" aria-hidden="true">
      <defs>
        <linearGradient id="pool-water-b" x1="0" y1="0" x2="1" y2="1">
          <stop offset="0" stop-color="var(--pool-light)"/>
          <stop offset="0.5" stop-color="var(--pool-mid)"/>
          <stop offset="1" stop-color="var(--pool-deep)"/>
        </linearGradient>
      </defs>
      <polygon class="band-water" role="img" aria-label="Pool water texture with umbrellas and pool floats"
               points="0,0 1060,0 1100,124 0,124"
               fill="url(#pool-water-b)"/>
      <line class="band-trim" x1="0" y1="2" x2="1060" y2="2" stroke="var(--trim)" stroke-width="4"/>
    </svg>
    <p class="phone">0491 358 217</p>
    <p class="brand-name">lakeshore tide care</p>
  </section>

</main>
</body>
</html>
```